Vital Metric Partners Ad for Healthcare Revolution

Half page advertisement:

size: W-8.5in H-5.5in
• be submitted as a PDF file at 300 DPI and in CMYK.
• No bleed
• Fonts should be converted to outlines and all images converted to CMYK with resolutions of 300 DPI.
• Images must be embedded
Unaccepted Formats:
PowerPoint, Ms Word, Publisher, PageMaker, Corel Draw

Color pallet:

231F20
646569
00A96C
F16362
FAA862
FEC35D

Website:
Vitalmetricpartners.example

Target Market(s)

Investors and business people

Font styles to use
Other font styles liked:
• Montserrat

Requirements
Must have
• The phrase "Take a simple concept and take it seriously" Dorian Feltwick, our website, contact information.
Nice to have
• Our logo which is on our website vitalmetricpartners.example. Color pallet:
• 231F20
• 646569
• 00A96C
• F16362
• FAA862
• FEC35D
• Website:
• Vitalmetricpartners.example
• Themes: Disruptive, Innovative, forward-thinking, proactive, empowering
• Our solution is scalable, and it makes sense now, we are at the right place at the right time, we are on the cusp of a breakthrough in healthcare.
• Briefly, here’s what we do:
• We work with individuals and businesses to identify lifestyle disease risk factors with the goal to improve health and reduce healthcare spending.
• Our mission is to reverse lifestyle disease by engaging, educating, and empowering people to understand and take control of their health. We believe it is critical to engage at an individual level to act effectively at a population level.
• We assess, analyze, and act.
• First, we assess individuals’ risk through our proprietary Vitality Score Gauge™ (VSG). We developed the VSG to be quantifiable, repeatable and to simplify biometric data to specifically address risk for developing lifestyle disease.
• Next, we assess the VSG data. Through our data analytics platform, we are able to find pain points and strategize interventions.
• Finally, we act upon the data to implement individual and population programs. We work with individuals, business owners, insurance brokers, and population health managers to create a culture that decreases risk factors through a variety of interventions including incentive programs, health coaching, education programs, and challenges.
• We repeat the process, enforcing the things that worked and modifying things that still need attention.
• Our “VSG-Based Wellness Approach” provides many downstream benefits. The VSG is a key metric for an individual’s lifestyle risk, population risk forecasting, financial incentives, and marketing.
Should not have
• We are the only ones doing this, or we are the best or we are a clear leader. Please avoid that.

```html
<!DOCTYPE html>
<html lang="en">
<head>
<meta charset="utf-8">
<title>Vital Metric Partners – Half Page Ad</title>
<link href="https://fonts.googleapis.com/css2?family=Catamaran:wght@800&family=Lato:wght@700&family=Montserrat:wght@400;500;700&family=Roboto+Condensed:ital,wght@0,300;0,400;0,700;1,300&display=swap" rel="stylesheet">
<style>
  :root {
    --ink: #231F20;
    --grey: #646569;
    --green: #00A96C;
    --coral: #F16362;
    --orange: #FAA862;
    --gold: #FEC35D;
    --backdrop: #2a2c37;
    --night: #2b2a2c;
    --white: #ffffff;
  }
  * { margin: 0; padding: 0; box-sizing: border-box; }
  html, body { width: 1200px; height: 1200px; overflow: hidden; }
  body { background: var(--backdrop); position: relative; }

  .ad {
    position: absolute; left: 63px; top: 253px;
    width: 1074px; height: 695px;
    background: var(--night); overflow: hidden;
  }
  .hero-photo {
    position: absolute; left: 470px; top: 0; width: 604px; height: 300px;
    background:
      linear-gradient(90deg, var(--night) 0%, rgba(43,42,44,0) 35%),
      linear-gradient(180deg, #8a7a6a 0%, #d9a95a 30%, #b98a3a 55%, #8f6a2a 100%);
  }
  .waves { position: absolute; left: 0; top: 0; }

  .portrait {
    position: absolute; left: 856px; top: 161px; width: 204px; height: 204px;
    border-radius: 50%; border: 4px solid var(--gold);
    background: radial-gradient(circle at 50% 40%, #f3e6de 0%, #d9c2b6 55%, #b5a79a 100%);
  }

  .brand {
    position: absolute; left: 45px; top: 62px;
    display: flex; align-items: center; gap: 12px;
  }
  .brand-dot { width: 30px; height: 30px; border-radius: 50%; background: var(--green); }
  .brand-name {
    font-family: "Montserrat", sans-serif; font-weight: 700;
    font-size: 34px; color: var(--white); letter-spacing: -0.5px;
  }

  .headline {
    position: absolute; left: 43px; top: 138px;
    font-family: "Catamaran", sans-serif; font-weight: 800;
    font-size: 57px; line-height: 51px; letter-spacing: 1px;
  }
  .headline .line-coral { color: var(--coral); display: block; }
  .headline .line-green { color: var(--green); display: block; }
  .tagline {
    position: absolute; left: 42px; top: 243px;
    font-family: "Lato", sans-serif; font-weight: 700;
    font-size: 27px; color: var(--white);
  }

  .copy {
    position: absolute; font-family: "Roboto Condensed", sans-serif;
    font-weight: 300; font-size: 12px; line-height: 17px; color: var(--grey);
    letter-spacing: -0.25px;
  }
  .copy p { margin-bottom: 9px; text-align: justify; }
  .col-left { left: 42px; top: 396px; width: 476px; }
  .col-right { left: 554px; top: 398px; width: 476px; }
  .col-right p { text-align: right; margin-bottom: 15px; }
  .col-right strong { font-weight: 700; color: var(--ink); }

  .section-title {
    position: relative; font-weight: 400; font-size: 26px; line-height: 30px;
    color: var(--green); letter-spacing: -0.3px; margin-bottom: 5px;
  }
  .section-title::before {
    content: ""; position: absolute; left: -17px; top: 2px;
    width: 4px; height: 26px; background: var(--orange);
  }
  .section-title.second { margin-top: 8px; }

  .divider {
    position: absolute; left: 538px; top: 423px; width: 1.5px; height: 188px;
    background: var(--ink);
  }

  .footer {
    position: absolute; left: 0; top: 626px; width: 1074px; height: 69px;
    background: var(--coral); color: var(--white);
    display: flex; flex-direction: column; align-items: center; justify-content: center; gap: 5px;
  }
  .footer .web { display: flex; align-items: center; gap: 14px; }
  .footer .url {
    font-family: "Montserrat", sans-serif; font-weight: 400; font-size: 18px;
    letter-spacing: 5.4px;
  }
  .footer .note {
    font-family: "Montserrat", sans-serif; font-weight: 500; font-size: 11px;
    letter-spacing: 0.4px; display: flex; gap: 22px;
  }
  .footer .quote { font-style: italic; }
</style>
</head>
<body>
  <div class="ad">
    <div class="hero-photo" role="img" aria-label="Photo of a woman with open arms in a golden field at sunset by the sea"></div>

    <svg class="waves" width="1074" height="695" viewBox="0 0 1074 695" aria-hidden="true">
      <path d="M0,290 Q520,335 1074,219 L1074,695 L0,695 Z" fill="var(--green)"/>
      <path d="M0,347 Q520,380 1074,231 L1074,695 L0,695 Z" fill="var(--coral)"/>
      <path d="M0,363 Q520,395 1074,243 L1074,695 L0,695 Z" fill="var(--white)"/>
    </svg>

    <div class="portrait" role="img" aria-label="Photo of a smiling older woman and her adult daughter embracing"></div>

    <div class="brand">
      <span class="brand-dot"></span>
      <span class="brand-name">Vital Metric Partners</span>
    </div>

    <h1 class="headline">
      <span class="line-coral">HARNESS THE POWER</span>
      <span class="line-green">OF HEALTH WITH VMP</span>
    </h1>
    <p class="tagline">Healthier people make healthier companies.</p>

    <div class="copy col-left">
      <h2 class="section-title">BRIEFLY, HERE’S WHAT WE DO:</h2>
      <p>We work with individuals and businesses to identify lifestyle disease risk factors with the goal to improve health and reduce healthcare spending.</p>
      <p>Our mission is to reverse lifestyle disease by engaging, educating, and empowering people to understand and take control of their health. We believe it is critical to engage at an individual level to act effectively at a population level.</p>
      <h2 class="section-title second">WE ASSESS, ANALYZE, AND ACT.</h2>
      <p>First, we assess individuals’ risk through our proprietary Vitality Score Gauge™ (VSG). We developed the VSG to be quantifiable, repeatable and to simplify biometric data to specifically address risk for developing lifestyle disease.</p>
    </div>

    <div class="divider"></div>

    <div class="copy col-right">
      <p>Next, we assess the VSG data. Through our data analytics platform, we are able to find pain points and strategize interventions.</p>
      <p>Finally, we act upon the data to implement individual and population programs. We work with individuals, business owners, insurance brokers, and population health managers to create a culture that decreases risk factors through a variety of interventions including incentive programs, health coaching, education programs, and challenges.</p>
      <p>We repeat the process, enforcing the things that worked and modifying things that still need attention.</p>
      <p>Our “<strong>VSG-Based Wellness Approach</strong>” provides many downstream benefits. The VSG is a key metric for an individual’s lifestyle risk, population risk forecasting, financial incentives, and marketing.</p>
    </div>

    <div class="footer">
      <div class="web">
        <svg width="20" height="20" viewBox="0 0 24 24" fill="none" stroke="var(--white)" stroke-width="1.8" aria-hidden="true">
          <circle cx="12" cy="12" r="10"/>
          <ellipse cx="12" cy="12" rx="4.5" ry="10"/>
          <line x1="2" y1="12" x2="22" y2="12"/>
          <path d="M4 6.5 H20 M4 17.5 H20"/>
        </svg>
        <span class="url">www.vitalmetricpartners.example</span>
      </div>
      <p class="note">
        <span class="quote">“Take a simple concept and take it seriously” — Dorian Feltwick</span>
        <span>(555) 010-2040</span>
        <span>info@vitalmetricpartners.example</span>
      </p>
    </div>
  </div>
</body>
</html>
```